Website for Nonprofit for kids whose parents have been wounded

We need a web design for a nonprofit that serves children who have been severely burned as well as those whose parents have been wounded during military service. We will be based out of hospitals and will need a format that will encourage trust, safety, and respect. We are stick with a lot of red white and blue. We will also be looking to have a space for donations.

Target Market(s)

Kids and parents of military veterans

Industry/Entity Type

Non Profit

Number of Pages Required

5+ page

Font styles to use
Serif
Decorative

Colors
ec1f27
ffffff
0255a3

Requirements
Must have
• Be both appealing to children and adults. Create a reputable face for our organization. We need an area for donations.
Nice to have
• Something unique

```html
<!DOCTYPE html>
<html lang="en">
<head>
<meta charset="utf-8">
<title>Hope Harbor — Kids of Wounded Service Members</title>
<link rel="stylesheet" href="https://fonts.googleapis.com/css2?family=Open+Sans:wght@300;400;600;700&family=Lora:wght@400;700&display=swap">
<style>
:root{
  --red:#ec1f27;
  --blue:#0255a3;
  --blue-dark:#04417d;
  --white:#ffffff;
  --page:#f1f1f1;
  --ink:#333333;
  --muted:#777777;
  --panel:#e6e6e6;
  --footer:#2f2f2f;
  --footer-deep:#222222;
  --footer-text:#a9a9a9;
}
*{box-sizing:border-box;margin:0;padding:0}
html,body{width:870px;height:1200px;overflow:hidden}
body{background:var(--page);font-family:"Open Sans",Arial,sans-serif;color:var(--ink);font-size:9px;line-height:1.45;position:relative}

/* header */
.site-header{top:0;height:92px;background:var(--white);left:0;width:870px;position:absolute}
.brand{position:absolute;left:60px;top:34px;display:flex;align-items:center;gap:8px}
.brand-square{width:16px;height:16px;background:var(--blue);display:block}
.brand-name{font-family:"Open Sans",Arial,sans-serif;font-weight:600;font-size:18px;color:var(--blue);line-height:1}
.search{position:absolute;right:44px;top:16px;display:flex}
.search-field{width:116px;height:15px;border:1px solid #cfcfcf;background:#fafafa}
.search-btn{height:15px;padding:0 8px;background:var(--blue);color:var(--white);font-size:7px;line-height:15px;font-weight:600}
.social{position:absolute;right:44px;top:38px;display:flex;gap:3px}
.social span{width:17px;height:17px;border-radius:2px;display:block}
.s1{background:#3b5998}.s2{background:#e04a2f}.s3{background:#2d8ad6}.s4{background:#f57d00}

.main-nav{position:absolute;top:96px;height:16px;left:40px;width:790px;background:var(--blue);display:flex;padding-left:18px}
.main-nav a{color:var(--white);text-decoration:none;font-size:7.5px;line-height:16px;padding:0 14px;font-weight:600}

/* hero */
.hero{position:absolute;top:130px;left:40px;width:497px;height:245px}
.hero-photo{position:absolute;inset:0;background:linear-gradient(135deg,#8fae5e 0%,#c9b28f 50%,#6d8a4a 100%)}
.hero-caption{position:absolute;left:0;bottom:0;width:100%;height:66px;background:rgba(20,20,20,.72);padding:10px 14px;color:var(--white)}
.hero-caption h2{font-size:11px;font-weight:600;margin-bottom:3px}
.hero-caption p{font-size:7px;color:#ddd}
.more{color:var(--red);font-size:7.5px;font-weight:600;display:inline-block;margin-top:3px}

.action-tiles{position:absolute;top:130px;left:560px;width:270px}
.tile{height:76px;margin-bottom:8px;display:flex}
.tile-photo{width:96px;height:100%}
.tile-label{flex:1;background:var(--blue);color:var(--white);font-family:"Lora",Georgia,serif;font-size:11px;text-align:center;display:flex;align-items:center;justify-content:center;letter-spacing:.5px;line-height:1.25;padding:0 10px}
.tp1{background:linear-gradient(135deg,#f39a3a,#d9563a)}
.tp2{background:linear-gradient(135deg,#5aa0d8,#2e6fae)}
.tp3{background:linear-gradient(135deg,#e05a4a,#f1c040 60%,#54a56a)}

/* feature cards */
.features{position:absolute;top:412px;left:40px;width:790px;display:flex;justify-content:space-between}
.card{width:250px;background:var(--white)}
.card-photo{height:140px}
.cp1{background:linear-gradient(135deg,#b7b1a8,#d8c8c0)}
.cp2{background:linear-gradient(135deg,#6b5a48,#c9a983)}
.cp3{background:linear-gradient(135deg,#a6774e,#e2c59d)}
.card-body{padding:14px 14px 12px;border-bottom:3px solid var(--red)}
.card-body h3{font-family:"Lora",Georgia,serif;color:var(--red);font-size:12px;font-weight:400;margin-bottom:6px}
.card-body p{font-size:6.8px;color:var(--muted)}

/* join band */
.join{position:absolute;top:708px;left:40px;width:790px;height:69px;background:var(--panel);padding:12px 20px}
.join h2{font-size:21px;font-weight:300;color:#555;line-height:1}
.join-rule{width:150px;height:2px;background:var(--red);margin:5px 0}
.join p{font-size:6.8px;color:var(--muted);width:320px}
.join-actions{position:absolute;right:24px;top:27px;display:flex;gap:12px}
.btn{background:var(--blue);color:var(--white);font-size:7.5px;font-weight:600;height:16px;line-height:16px;padding:0 22px;border-radius:2px}

/* events */
.events{position:absolute;top:806px;left:40px;width:790px;display:flex;gap:12px}
.events-intro{width:180px;height:164px;background:var(--panel);padding:12px}
.events-intro h3{font-size:11px;font-weight:600;color:#555;margin-bottom:5px}
.events-intro p{font-size:6.8px;color:var(--muted)}
.event{width:190px}
.event-photo{height:104px;margin-bottom:6px}
.ep1{background:linear-gradient(135deg,#7d8ea8,#c5b6a6)}
.ep2{background:linear-gradient(135deg,#7aa0c8,#d5c3a4)}
.ep3{background:linear-gradient(135deg,#5c6f8c,#e0cfb6)}
.event p{font-size:6.8px;color:var(--muted)}

/* footer */
.site-footer{position:absolute;top:995px;left:0;width:870px;height:150px;background:var(--footer)}
.footer-cols{position:absolute;left:40px;top:18px;width:790px;display:flex;gap:20px}
.fcol{width:182px}
.fcol h4{color:var(--white);font-size:7.5px;font-weight:700;text-transform:uppercase;margin-bottom:6px}
.fcol p,.fcol li{font-size:6.3px;color:var(--footer-text)}
.fcol ul{list-style:none}
.fcol li{padding:2.5px 0;border-bottom:1px solid #3d3d3d}
.fcol li::before{content:"› ";color:var(--red)}
.post{margin-bottom:6px}
.post b{color:var(--red);font-weight:600}
.form-row{display:flex;margin-bottom:4px;align-items:center}
.form-row span{width:44px;font-size:6.3px;color:var(--footer-text)}
.form-row i{flex:1;height:12px;background:#444;border:1px solid #555;display:block}
.form-row i.tall{height:26px}
.submit{margin-left:44px;background:#555;color:var(--white);font-size:6.3px;padding:2px 10px;display:inline-block}
.copyright{position:absolute;top:1145px;left:0;width:870px;height:55px;background:var(--footer-deep);color:#888;font-size:6.5px;text-align:center;padding-top:12px}
</style>
</head>
<body>

<header class="site-header">
  <div class="brand">
    <span class="brand-square"></span>
    <span class="brand-name">Hope Harbor</span>
  </div>
  <div class="search"><span class="search-field"></span><span class="search-btn">Search</span></div>
  <div class="social" aria-label="Social links"><span class="s1"></span><span class="s2"></span><span class="s3"></span><span class="s4"></span></div>
</header>

<nav class="main-nav">
  <a>Home</a><a>About Us</a><a>Services</a><a>Donations</a><a>Blog</a><a>Contact Us</a>
</nav>

<section class="hero">
  <div class="hero-photo" role="img" aria-label="Photo of a smiling child outdoors"></div>
  <div class="hero-caption">
    <h2>Nullam laoreet dui ipsum</h2>
    <p>Suspendisse sit amet congue odio non erat vulputate, at tempus nunc viverra.</p>
    <span class="more">Learn More »</span>
  </div>
</section>

<aside class="action-tiles">
  <div class="tile"><div class="tile-photo tp1" role="img" aria-label="Children at a program activity"></div><div class="tile-label">PROGRAMS</div></div>
  <div class="tile"><div class="tile-photo tp2" role="img" aria-label="Hands placing a donation"></div><div class="tile-label">MAKE A DONATION</div></div>
  <div class="tile"><div class="tile-photo tp3" role="img" aria-label="Raised hands of volunteers"></div><div class="tile-label">BECOME A VOLUNTEER</div></div>
</aside>

<section class="features">
  <article class="card">
    <div class="card-photo cp1" role="img" aria-label="Child sitting by a wall"></div>
    <div class="card-body"><h3>Vivamus libero augue</h3><p>Lorem ipsum dolor sit amet, consectetur adipiscing elit. Integer pellentesque dui et tortor porttitor, non cursus arcu aliquet.</p><span class="more">Read More »</span></div>
  </article>
  <article class="card">
    <div class="card-photo cp2" role="img" aria-label="Child reading by a window"></div>
    <div class="card-body"><h3>Vivamus libero augue</h3><p>Lorem ipsum dolor sit amet, consectetur adipiscing elit. Integer pellentesque dui et tortor porttitor, non cursus arcu aliquet.</p><span class="more">Read More »</span></div>
  </article>
  <article class="card">
    <div class="card-photo cp3" role="img" aria-label="Children reading a book together"></div>
    <div class="card-body"><h3>Vivamus libero augue</h3><p>Lorem ipsum dolor sit amet, consectetur adipiscing elit. Integer pellentesque dui et tortor porttitor, non cursus arcu aliquet.</p><span class="more">Read More »</span></div>
  </article>
</section>

<section class="join">
  <h2>Join With Us</h2>
  <div class="join-rule"></div>
  <p>Lorem ipsum dolor sit amet, consectetur adipiscing elit. Nullam blandit nunc vitae arcu tempor, sit amet dictum mi feugiat.</p>
  <div class="join-actions"><span class="btn">Make a Donation</span><span class="btn">Volunteer</span></div>
</section>

<section class="events">
  <div class="events-intro">
    <h3>Events</h3>
    <p>Lorem ipsum dolor sit amet, consectetur adipiscing elit. Integer pellentesque dui et tortor porttitor, non cursus arcu aliquet. Donec vitae justo sed nibh lacinia tempor at ut nunc. Morbi sit amet risus.</p>
    <span class="more">Read More »</span>
  </div>
  <div class="event"><div class="event-photo ep1" role="img" aria-label="Family gathering at an event"></div><p>Quisque velit lectus ut convallis sollicitudin id nunc.</p><span class="more">Read More »</span></div>
  <div class="event"><div class="event-photo ep2" role="img" aria-label="Kids at an outdoor event"></div><p>Quisque velit lectus ut convallis sollicitudin id nunc.</p><span class="more">Read More »</span></div>
  <div class="event"><div class="event-photo ep3" role="img" aria-label="Volunteers with children at a party"></div><p>Quisque velit lectus ut convallis sollicitudin id nunc.</p><span class="more">Read More »</span></div>
</section>

<footer class="site-footer">
  <div class="footer-cols">
    <div class="fcol">
      <h4>About Us</h4>
      <p>Lorem ipsum dolor sit amet, consectetur adipiscing elit. Integer pellentesque dui et tortor porttitor non cursus arcu. Donec vitae justo sed nibh lacinia tempor. Morbi sit amet risus vel nunc feugiat.</p>
    </div>
    <div class="fcol">
      <h4>Quick Links</h4>
      <ul><li>Lorem ipsum dolor</li><li>Consectetur elit</li><li>Integer pellentesque</li><li>Donec vitae justo</li><li>Morbi sit amet</li><li>Nullam blandit nunc</li></ul>
    </div>
    <div class="fcol">
      <h4>Latest Posts</h4>
      <p class="post"><b>May 12</b> Lorem ipsum dolor sit amet consectetur adipiscing elit integer.</p>
      <p class="post"><b>May 04</b> Donec vitae justo sed nibh lacinia tempor morbi sit.</p>
      <p class="post"><b>Apr 28</b> Nullam blandit nunc vitae arcu tempor dictum.</p>
    </div>
    <div class="fcol">
      <h4>Contact Us</h4>
      <div class="form-row"><span>Name</span><i></i></div>
      <div class="form-row"><span>Email</span><i></i></div>
      <div class="form-row"><span>Message</span><i class="tall"></i></div>
      <span class="submit">Submit</span>
    </div>
  </div>
</footer>
<div class="copyright">Copyright © 2014 Hope Harbor | All Rights Reserved</div>

</body>
</html>
```